Aerial Imaging and photgraphy business card

Design a business card with eye catching aerial photo of country side / landscape with a drone in the foreground.
Also contact details.

Target Market(s)

Aerial Imaging photography

Industry/Entity Type

Advertising

Contact Information for Business Card

Corwin
0412905316
Website http://www.skylarkvistas.com.au/
email address : skylarkvistas.com.au

Colors
e8f1ca
cadf82
9bcb3c
33a6d7
85cae6
cee9f5

Requirements
Must have
• High res photo
• KPV drone in the foreground Either T4200 and kpv Hovera or both
Nice to have
• high resolution landscape country photo on the front of the card with a KPV T4200 drone in the foreground.

```html
<!DOCTYPE html>
<html lang="en">
<head>
<meta charset="utf-8">
<title>Skylark Vistas – Business Card</title>
<link href="https://fonts.googleapis.com/css2?family=Arimo:wght@400;700&display=swap" rel="stylesheet">
<style>
  :root {
    --bg: #e9e6e1;
    --card-white: #fbfbfb;
    --ink: #1d1d1d;
    --ink-soft: #3a3a3a;
    --brand: #2f3a44;
    --sky-top: #cfe2f0;
    --sky-mid: #e6eef3;
    --field: #a7a98a;
    --field-dark: #6f6a55;
    --water: #9fb6c4;
    --edge: #4c86ad;
  }
  * { margin: 0; padding: 0; box-sizing: border-box; }
  html, body { width: 1200px; height: 902px; overflow: hidden; }
  body {
    background: var(--bg);
    font-family: "Arimo", Arial, sans-serif;
    color: var(--ink);
    position: relative;
  }
  .card {
    position: absolute;
    left: 320px;
    width: 560px;
    height: 320px;
    border-radius: 4px;
    box-shadow: 0 6px 18px rgba(0,0,0,0.18);
    overflow: hidden;
  }
  .card-front { top: 110px; background: var(--card-white); }
  .card-back { top: 470px; }

  .wordmark {
    display: flex;
    align-items: center;
    gap: 12px;
    font-weight: 700;
    color: var(--brand);
    text-transform: uppercase;
    letter-spacing: 1px;
  }
  .wordmark-dot {
    border-radius: 50%;
    background: var(--brand);
    flex: none;
  }
  .card-front .wordmark {
    position: absolute;
    left: 50%; top: 50%;
    transform: translate(-50%, -50%);
    font-size: 34px;
  }
  .card-front .wordmark-dot { width: 22px; height: 22px; }

  .landscape-photo {
    position: absolute; inset: 0;
    background: linear-gradient(180deg,
      var(--sky-top) 0%, var(--sky-mid) 35%,
      var(--field) 52%, var(--water) 68%, var(--field-dark) 100%);
  }
  .photo-veil { position: absolute; inset: 0; background: rgba(255,255,255,0.35); }
  .card-back .wordmark {
    position: absolute;
    left: 40px; top: 150px;
    font-size: 24px;
  }
  .card-back .wordmark-dot { width: 16px; height: 16px; }

  .divider {
    position: absolute;
    left: 300px; top: 22px;
    width: 2px; height: 276px;
    background: var(--ink);
  }
  .person { position: absolute; left: 322px; top: 34px; }
  .person-name { font-size: 17px; font-weight: 700; }
  .person-role { font-size: 13px; color: var(--ink-soft); margin-top: 2px; padding-left: 10px; }

  .contact-list {
    position: absolute;
    left: 322px; top: 178px;
    list-style: none;
    font-size: 13px;
  }
  .contact-list li {
    display: flex; align-items: center; gap: 10px;
    height: 24px;
  }
  .contact-icon {
    width: 16px; height: 16px;
    background: var(--ink);
    border-radius: 2px;
    display: flex; align-items: center; justify-content: center;
    flex: none;
  }
</style>
</head>
<body>

<section class="card card-front">
  <div class="wordmark"><span class="wordmark-dot"></span>Skylark Vistas</div>
</section>

<section class="card card-back">
  <div class="landscape-photo" role="img" aria-label="Aerial photograph of green countryside with a river, wooded hills and a pale blue sky"></div>
  <div class="photo-veil"></div>

  <div class="wordmark"><span class="wordmark-dot"></span>Skylark Vistas</div>

  <div class="divider"></div>

  <div class="person">
    <div class="person-name">Corwin Hale</div>
    <div class="person-role">Owner</div>
  </div>

  <ul class="contact-list">
    <li>
      <span class="contact-icon"><svg width="10" height="10" viewBox="0 0 10 10"><path d="M2 1 L4 1 L4.6 3 L3.4 3.8 Q4.4 5.8 6.2 6.6 L7 5.4 L9 6 L9 8 Q8.5 9 7.5 9 Q1 8 1 2.5 Q1 1 2 1Z" fill="#fff"/></svg></span>
      0412905316
    </li>
    <li>
      <span class="contact-icon"><svg width="10" height="8" viewBox="0 0 10 8"><rect x="0.5" y="0.5" width="9" height="7" fill="none" stroke="#fff"/><path d="M0.5 0.5 L5 4.5 L9.5 0.5" fill="none" stroke="#fff"/></svg></span>
      info@skylarkvistas.com.au
    </li>
    <li>
      <span class="contact-icon"><svg width="10" height="10" viewBox="0 0 10 10"><circle cx="5" cy="5" r="4" fill="none" stroke="#fff"/><path d="M1 5 H9 M5 1 Q2.5 5 5 9 M5 1 Q7.5 5 5 9" fill="none" stroke="#fff" stroke-width="0.8"/></svg></span>
      www.skylarkvistas.com
    </li>
    <li>
      <span class="contact-icon"><svg width="8" height="11" viewBox="0 0 8 11"><path d="M4 0.5 Q7.5 0.5 7.5 4 Q7.5 6.5 4 10.5 Q0.5 6.5 0.5 4 Q0.5 0.5 4 0.5Z" fill="#fff"/><circle cx="4" cy="4" r="1.4" fill="#1d1d1d"/></svg></span>
      Bellmount NSW 2590, Australia
    </li>
  </ul>
</section>

</body>
</html>
```